PELDRAX Business Cards

We require a business card for our company that provides IT consulting services. We already have a logo that needs to be used on the card. We want a clean professional looking design that incorporates our colours. Our main focus is providing managed services to business, which involves us looking after all of their IT requirements including managing servers/networks, projects, and procurement.

Industry/Entity Type

Information Technology

Requirements
Must have
• our logo, contact information, name, title, phone numbers

```html
<!DOCTYPE html>
<html lang="en">
<head>
<meta charset="utf-8">
<title>PELDRAX Business Cards</title>
<link href="https://fonts.googleapis.com/css2?family=Questrial&family=Open+Sans:wght@400;600&display=swap" rel="stylesheet">
<style>
  :root {
    --brand-blue: #0b8fd1;
    --brand-blue-deep: #077bb6;
    --card-grey: #dedede;
    --ink: #333333;
    --white: #ffffff;
    --stage: #3b3b3d;
  }
  * { box-sizing: border-box; margin: 0; padding: 0; }
  html, body { width: 1200px; height: 896px; overflow: hidden; }
  body {
    background: var(--stage);
    display: flex;
    flex-direction: column;
    align-items: center;
    justify-content: center;
    gap: 50px;
    font-family: "Open Sans", sans-serif;
  }
  .card {
    position: relative;
    width: 660px;
    height: 377px;
    overflow: hidden;
  }

  /* ---------- Front: contact side ---------- */
  .card--front { background: var(--card-grey); }
  .card--front .accent-band {
    position: absolute; left: 0; right: 0; bottom: 0; height: 16px;
    background: var(--brand-blue);
  }
  .card--front .mark-watermark {
    position: absolute; left: 120px; top: -40px; width: 360px; height: 300px;
    background: radial-gradient(ellipse at 40% 40%, rgba(255,255,255,0.55), rgba(255,255,255,0) 70%);
  }
  .person { position: absolute; left: 46px; top: 58px; }
  .person__name {
    font-family: "Questrial", sans-serif;
    color: var(--brand-blue);
    font-size: 27px; font-weight: 700; letter-spacing: 1px;
    text-transform: uppercase;
  }
  .person__title { color: var(--ink); font-size: 16px; margin-top: 2px; }
  .address { position: absolute; left: 46px; top: 140px; color: var(--ink); font-size: 15px; line-height: 1.45; }

  .brand {
    display: flex; align-items: center; gap: 14px;
    font-family: "Questrial", sans-serif;
    letter-spacing: 4px;
  }
  .brand__dot { width: 44px; height: 44px; border-radius: 50%; }
  .card--front .brand { position: absolute; right: 46px; top: 118px; color: var(--brand-blue); font-size: 60px; }
  .card--front .brand__dot { background: var(--brand-blue); }

  .divider { position: absolute; height: 1px; background: rgba(0,0,0,0.12); }
  .card--front .divider { left: 46px; right: 46px; top: 225px; }

  .contacts {
    position: absolute; right: 46px; top: 248px;
    list-style: none; text-align: right; color: var(--ink); font-size: 16px; line-height: 1.5;
  }
  .contacts li { display: flex; justify-content: flex-end; align-items: center; gap: 10px; }
  .contacts svg { width: 15px; height: 15px; fill: var(--brand-blue); }

  /* ---------- Back: services side ---------- */
  .card--back { background: var(--brand-blue); }
  .card--back .mark-watermark {
    position: absolute; left: 60px; top: -20px; width: 360px; height: 320px;
    background: radial-gradient(ellipse at 50% 45%, rgba(255,255,255,0.16), rgba(255,255,255,0) 70%);
  }
  .card--back .brand { position: absolute; left: 50%; top: 70px; transform: translateX(-50%); color: var(--white); font-size: 64px; }
  .card--back .brand__dot { background: var(--white); }
  .social { position: absolute; left: 50%; top: 170px; transform: translateX(-50%); display: flex; gap: 8px; }
  .social span { width: 22px; height: 22px; border-radius: 50%; background: var(--white); }
  .card--back .divider { left: 46px; right: 46px; top: 212px; background: rgba(255,255,255,0.35); }
  .services {
    position: absolute; left: 0; right: 0; top: 236px;
    color: var(--white); text-align: center;
    font-family: "Questrial", sans-serif; font-size: 16px; letter-spacing: 1px;
    text-transform: uppercase; line-height: 1.9;
  }
  .services .sep { margin: 0 12px; }
</style>
</head>
<body>

  <section class="card card--front" aria-label="Business card, contact side">
    <div class="mark-watermark" role="img" aria-label="Faint brand mark decoration"></div>
    <div class="person">
      <p class="person__name">Daniel Ostrander</p>
      <p class="person__title">President &amp; Technology Consultant</p>
    </div>
    <p class="address">48 Cedar Lane<br>Box 902, Maple Ridge, AB</p>
    <div class="brand"><span class="brand__dot"></span><span>PELDRAX</span></div>
    <div class="divider"></div>
    <ul class="contacts">
      <li>555-013-2848
        <svg viewBox="0 0 16 16"><path d="M3 1h3l1.5 4-2 1.2a9 9 0 0 0 4.3 4.3l1.2-2 4 1.5v3a2 2 0 0 1-2 2A13 13 0 0 1 1 3a2 2 0 0 1 2-2z"/></svg>
      </li>
      <li>info@peldrax.com
        <svg viewBox="0 0 16 16"><path d="M1 3h14v10H1z M2 4l6 5 6-5" fill="none" stroke="#0b8fd1" stroke-width="1.6"/></svg>
      </li>
      <li>www.peldrax.com
        <svg viewBox="0 0 16 16"><circle cx="8" cy="8" r="6.5" fill="none" stroke="#0b8fd1" stroke-width="1.5"/><path d="M1.5 8h13M8 1.5c-3 3.5-3 9.5 0 13M8 1.5c3 3.5 3 9.5 0 13" fill="none" stroke="#0b8fd1" stroke-width="1.2"/></svg>
      </li>
    </ul>
    <div class="accent-band"></div>
  </section>

  <section class="card card--back" aria-label="Business card, services side">
    <div class="mark-watermark" role="img" aria-label="Faint brand mark decoration"></div>
    <div class="brand"><span class="brand__dot"></span><span>PELDRAX</span></div>
    <div class="social" aria-label="Social media links"><span></span><span></span><span></span><span></span><span></span></div>
    <div class="divider"></div>
    <div class="services">
      <p>Infrastructure Design<span class="sep">/</span>Cloud Integration<span class="sep">/</span>IT Assessments</p>
      <p>Data Protection<span class="sep">/</span>Mobility Solutions<span class="sep">/</span>Desktop Support<span class="sep">/</span>Network Design</p>
    </div>
  </section>

</body>
</html>
```